Flyer Design Project

We are offering a new class on cyber crime and want to advertise this course to students. We would like to see a design that is eye catching and coveys the goals of the course, when it meets and a brief abstract for the class.

The course will focus on the economics of cyber crime so including one or two graphics that get across this point would be good.

Requirements
Must have
• Course name "Cyber Crime"
Call number "CS 795 - 004"
Course meeting time (day of week and time) Tue. 4:30-7:10pm
Course goals
Course abstract

```html
<!DOCTYPE html>
<html lang="en">
<head>
<meta charset="utf-8">
<title>Cyber Crime — Course Flyer</title>
<link rel="stylesheet" href="https://fonts.googleapis.com/css2?family=Anton&family=Arimo:wght@400;700&family=Didact+Gothic&display=swap">
<style>
  :root {
    --ink: #000000;
    --paper: #ffffff;
    --night: #02060f;
    --glow-deep: #041a4a;
    --glow-mid: #0c4ea8;
    --glow-bright: #7fd2ff;
    --band-yellow: #fff200;
    --band-orange: #f7941d;
    --title-yellow: #ffe600;
    --title-orange: #f6a21a;
    --title-red: #e3231b;
    --link-yellow: #ffe600;
  }
  * { margin: 0; padding: 0; box-sizing: border-box; }
  html, body { width: 927px; height: 1200px; overflow: hidden; background: var(--ink); }
  .flyer {
    position: relative;
    width: 927px;
    height: 1200px;
    background: var(--ink);
    color: var(--paper);
    font-family: "Didact Gothic", "Century Gothic", sans-serif;
    overflow: hidden;
  }
  .hero-image {
    position: absolute;
    left: 0; top: 0;
    width: 927px; height: 533px;
    background:
      radial-gradient(ellipse 55% 38% at 50% 30%, var(--glow-bright) 0%, var(--glow-mid) 40%, transparent 75%),
      linear-gradient(180deg, var(--night) 0%, var(--glow-deep) 40%, var(--glow-mid) 70%, var(--glow-deep) 100%);
  }
  .course-title {
    position: absolute;
    left: 0; top: 40px;
    width: 927px; height: 220px;
  }
  .course-title text {
    font-family: "Anton", "Impact", sans-serif;
    font-size: 158px;
    paint-order: stroke;
  }
  .info-band {
    position: absolute;
    left: 0; top: 533px;
    width: 927px; height: 70px;
    background: linear-gradient(90deg, var(--band-yellow) 0%, #ffd21a 45%, var(--band-orange) 100%);
    color: var(--ink);
  }
  .info-item { position: absolute; top: 13px; }
  .info-item.number { left: 120px; }
  .info-item.time { left: 388px; }
  .info-label {
    font-family: "Arimo", Arial, sans-serif;
    font-weight: 700;
    font-size: 19px;
    line-height: 24px;
  }
  .info-value { font-size: 16px; line-height: 24px; }
  .section-heading {
    position: absolute;
    left: 64px;
    font-family: "Arimo", Arial, sans-serif;
    font-weight: 700;
    font-size: 21px;
  }
  .goals-heading { top: 650px; }
  .goal-list {
    position: absolute;
    left: 64px; top: 693px;
    width: 540px;
    list-style: none;
    font-size: 18.5px;
    line-height: 22px;
  }
  .goal-list li + li { margin-top: 11px; }
  .abstract-heading { top: 876px; }
  .abstract-text {
    position: absolute;
    left: 64px; top: 911px;
    width: 598px;
    font-size: 18.5px;
    line-height: 22px;
    text-align: justify;
  }
  .course-link {
    position: absolute;
    left: 64px; top: 1138px;
    font-family: "Arimo", Arial, sans-serif;
    font-weight: 700;
    font-size: 24px;
    color: var(--link-yellow);
    text-decoration: none;
  }
</style>
</head>
<body>
<main class="flyer">
  <div class="hero-image" role="img" aria-label="Glowing blue digital tunnel of binary code with computer monitors and hands typing on keyboards"></div>

  <svg class="course-title" viewBox="0 0 927 220" aria-label="Cyber Crime">
    <defs>
      <linearGradient id="title-fill" x1="0" y1="0" x2="0" y2="1">
        <stop offset="0" stop-color="var(--title-yellow)"/>
        <stop offset="1" stop-color="var(--title-orange)"/>
      </linearGradient>
    </defs>
    <text x="463" y="190" text-anchor="middle" textLength="697" lengthAdjust="spacingAndGlyphs"
          fill="url(#title-fill)" stroke="var(--title-red)" stroke-width="9" stroke-linejoin="round">Cyber Crime</text>
  </svg>

  <section class="info-band">
    <div class="info-item number">
      <p class="info-label">Cource Number</p>
      <p class="info-value">CS 795 / ISA 797</p>
    </div>
    <div class="info-item time">
      <p class="info-label">Course Meeting Time</p>
      <p class="info-value">Fall 2012 (day of week and time) Tue. 4:30-7:10pm</p>
    </div>
  </section>

  <h2 class="section-heading goals-heading">The Goal of the Class:</h2>
  <ol class="goal-list">
    <li>1) Understand how modern cyber-crime operates on a technical and economic level.</li>
    <li>2) Analyze some of the potential places to intervene at an economic, technical and policy level.</li>
  </ol>

  <h2 class="section-heading abstract-heading">Course Abstract:</h2>
  <p class="abstract-text">Arguably the single most significant change in the cyber-security landscape has been the explosive rise of profit-fueled cyber-crime. Obtaining a detailed, structural understanding of how profit-driven cyber crime works — its underlying economics and associated business practices — has the potential to illuminate new defensive measures that might prove far more efficient for countering attacks than purely technical measures. This research seminar will delve into our current understanding of the economics of cyber-crime.</p>

  <a class="course-link" href="#">http://cs.northfield.edu/~rivera/crime.html</a>
</main>
</body>
</html>
```